Visitenkarten-Design für Psycho-Kinesiologie Praxis
Zielgruppe
praxis für Psycho-Kinesiologie - Systematische Familienaufstellungen. Einzelsitzungen Gruppentherapie
Ich suche ein Design was auf der einen Seite auffällt, aus dem Rahmen fällt und trotzdem seriös wirkt und Vertrauen schafft.
Die Anhänge sind nur meine Entwürfe also keine fixen Vorgaben
Aufgabenstellung
Eine Seite soll auffallen und Kreativ gestaltet sein
Es gibt ein Template aber die Farben sind noch nicht definiert.
https://www.vorlagenhafen.com/de/demo/48352.html
Es gibt ein Logo (Systemanalytiker) da sind die Farben auch nicht fix Definiert. Gerne sehe ich verschiedene Farbkombinationen
Foto: besseres folgt in kürze
Lumen Harbor Circle: Kann auf einer Seite drauf sein, wenn genug Platz,

```html
<!DOCTYPE html>
<html lang="de">
<head>
<meta charset="utf-8">
<title>Seelenweg – Visitenkarten</title>
<link rel="stylesheet" href="https://fonts.googleapis.com/css2?family=Jost:wght@300;400&family=Lora:ital,wght@0,500;1,500&display=swap">
<style>
:root{
  --page:#ffffff;
  --charcoal:#2a2d30;
  --charcoal-soft:#353a3e;
  --band:#4a4d50;
  --red:#a51e2e;
  --red-line:#c3202f;
  --white:#ffffff;
  --muted:#c9cbcd;
  --violet:#8a1a9a;
  --photo-a:#9b9b9b;
  --photo-b:#d8d8d8;
}
*{box-sizing:border-box;margin:0;padding:0}
html,body{width:857px;height:1200px;overflow:hidden;background:var(--page)}
body{position:relative;font-family:"Jost",sans-serif;color:var(--white)}
.card{position:absolute;width:238px;height:154px;overflow:hidden;box-shadow:1px 2px 4px rgba(0,0,0,.35)}
.card--front{left:181px;background:var(--charcoal)}
.card--back{left:444px;background:var(--charcoal)}
.motto{position:absolute;left:0;right:0;bottom:0;height:12px;background:var(--band);border-top:1.5px solid var(--red-line);font-size:7px;letter-spacing:1.6px;text-align:center;line-height:11px;font-weight:400}
.arc{position:absolute;right:-28px;top:6px;width:140px;height:140px;border-radius:50%;border:10px solid var(--charcoal-soft);border-left-color:transparent;border-bottom-color:transparent;transform:rotate(20deg)}
.pattern{position:absolute;right:6px;top:6px;width:116px;height:116px;border-radius:50%;background:radial-gradient(circle,rgba(138,26,154,.35),rgba(138,26,154,.12) 70%,transparent 72%)}
.lettering{position:absolute;left:6px;top:40px;width:110px;height:92px;background:linear-gradient(160deg,rgba(138,26,154,.55),rgba(138,26,154,.2));border-radius:4px}
.brand{position:absolute;display:flex;align-items:center;gap:5px;font-weight:300;color:var(--white);line-height:1}
.brand__dot{width:9px;height:9px;border-radius:50%;background:var(--red-line);flex:none}
.brand--front{left:36px;top:54px;font-size:28px}
.brand--front .brand__dot{width:14px;height:14px}
.brand-sub{position:absolute;font-weight:300;color:var(--muted);font-size:6px}
.brand-sub--front{left:152px;top:91px}
.services{position:absolute;left:0;right:0;top:106px;font-size:6px;text-align:center;line-height:8.5px}
.front-name{position:absolute;right:37px;top:106px;font-size:12px;font-weight:300}
.panel{position:absolute;top:0;left:0;width:119px;height:142px;background:var(--red)}
.photo{position:absolute;top:0;left:119px;width:119px;height:142px;background:linear-gradient(110deg,var(--photo-a),var(--photo-b) 55%,#b8b8b8)}
.brand--panel{left:9px;top:20px;font-size:17px}
.brand-sub--panel{left:69px;top:40px;font-size:4px}
.person{position:absolute;left:11px;top:58px}
.person__name{font-family:"Lora",serif;font-weight:500;font-size:9.5px}
.person__role{font-size:7px;font-weight:300;margin-top:1px}
.contacts{position:absolute;left:10px;list-style:none;font-size:5.8px;line-height:7.9px;font-weight:300}
.contacts li{display:flex;align-items:center;gap:3px}
.contacts .ic{width:6px;height:6px;flex:none}
.contacts .gap{padding-left:9px}
.contacts--photo{top:91px}
.badge{position:absolute;display:flex;align-items:center;gap:3px;font-size:5.2px;font-weight:400;letter-spacing:.2px}
.badge__mark{width:14px;height:14px;border-radius:50%;background:var(--red-line);flex:none}
.badge--photo{right:4px;bottom:17px;color:var(--charcoal)}
.badge--dark{right:6px;bottom:18px;color:var(--white)}
.svc-list{position:absolute;left:9px;top:14px;list-style:none;font-size:6px;line-height:9px;font-weight:300}
.svc-list li{border-left:1px solid var(--white);padding-left:2px}
.svc-list li.cont{border-left:none;padding-left:3px}
.contacts--dark{top:90px}
.brand--dark{left:124px;top:24px;font-size:18px}
.brand-sub--dark{left:183px;top:52px;font-size:4px}
.person--dark{left:125px;top:76px}
.person--dark .person__name{font-style:italic}
</style>
</head>
<body>

<!-- Row 1 -->
<section class="card card--front" style="top:45px">
  <div class="pattern" role="img" aria-label="Dekoratives Blume-des-Lebens-Muster in Violett"></div>
  <div class="lettering" role="img" aria-label="Handschriftzug in Violett"></div>
  <div class="brand brand--front"><span class="brand__dot"></span>Seelenweg</div>
  <div class="brand-sub brand-sub--front">Systemanalytiker</div>
  <p class="services">Psycho-Kinesiologie nach Dr. Kellermann | Neurobiologie<br>Mentalfeldtherapie | Geistiges Familienstellen</p>
  <div class="motto">Gesundheit - Glück - Liebe - Frieden</div>
</section>
<section class="card card--back" style="top:45px">
  <div class="panel"></div>
  <div class="photo" role="img" aria-label="Schwarzweiß-Porträtfoto des Systemanalytikers"></div>
  <div class="brand brand--panel"><span class="brand__dot"></span>Seelenweg</div>
  <div class="brand-sub brand-sub--panel">Systemanalytiker</div>
  <div class="person"><div class="person__name">Udo Falkner</div><div class="person__role">Systemanalytiker</div></div>
  <ul class="contacts contacts--photo">
    <li><svg class="ic" viewBox="0 0 10 10"><path d="M2 1l2 2-1 1.5c.8 1.5 1.5 2.2 3 3L7.5 6l2 2-1.3 1.5C4.5 9 1 5.5.5 1.8z" fill="#fff"/></svg>Schweiz</li>
    <li class="gap">0041 790 482 615</li>
    <li><svg class="ic" viewBox="0 0 10 10"><path d="M2 1l2 2-1 1.5c.8 1.5 1.5 2.2 3 3L7.5 6l2 2-1.3 1.5C4.5 9 1 5.5.5 1.8z" fill="#fff"/></svg>Deutschland</li>
    <li class="gap">0049 170 264 81 93</li>
    <li><svg class="ic" viewBox="0 0 10 10"><rect x=".5" y="2" width="9" height="6" fill="#fff"/><path d="M.5 2l4.5 3.5L9.5 2" stroke="#a51e2e" fill="none"/></svg>info@seelenweg-praxis.ch</li>
    <li><svg class="ic" viewBox="0 0 10 10"><circle cx="5" cy="5" r="4" stroke="#fff" fill="none"/><path d="M1 5h8M5 1c-2 2.5-2 5.5 0 8M5 1c2 2.5 2 5.5 0 8" stroke="#fff" fill="none" stroke-width=".7"/></svg>www.seelenweg-praxis.ch</li>
  </ul>
  <div class="badge badge--photo"><span class="badge__mark"></span>Lumen Harbor Circle</div>
  <div class="motto">Gesundheit - Glück - Liebe - Frieden</div>
</section>

<!-- Row 2 -->
<section class="card card--front" style="top:236px">
  <div class="arc"></div>
  <div class="brand brand--front"><span class="brand__dot"></span>Seelenweg</div>
  <div class="brand-sub brand-sub--front">Systemanalytiker</div>
  <p class="services">Psycho-Kinesiologie nach Dr. Kellermann | Neurobiologie<br>Mentalfeldtherapie | Geistiges Familienstellen</p>
  <div class="motto">Gesundheit - Glück - Liebe - Frieden</div>
</section>
<section class="card card--back" style="top:236px">
  <div class="panel"></div>
  <div class="photo" role="img" aria-label="Schwarzweiß-Porträtfoto des Systemanalytikers"></div>
  <div class="brand brand--panel"><span class="brand__dot"></span>Seelenweg</div>
  <div class="brand-sub brand-sub--panel">Systemanalytiker</div>
  <div class="person"><div class="person__name">Udo Falkner</div><div class="person__role">Systemanalytiker</div></div>
  <ul class="contacts contacts--photo">
    <li><svg class="ic" viewBox="0 0 10 10"><path d="M2 1l2 2-1 1.5c.8 1.5 1.5 2.2 3 3L7.5 6l2 2-1.3 1.5C4.5 9 1 5.5.5 1.8z" fill="#fff"/></svg>Schweiz</li>
    <li class="gap">0041 790 482 615</li>
    <li><svg class="ic" viewBox="0 0 10 10"><path d="M2 1l2 2-1 1.5c.8 1.5 1.5 2.2 3 3L7.5 6l2 2-1.3 1.5C4.5 9 1 5.5.5 1.8z" fill="#fff"/></svg>Deutschland</li>
    <li class="gap">0049 170 264 81 93</li>
    <li><svg class="ic" viewBox="0 0 10 10"><rect x=".5" y="2" width="9" height="6" fill="#fff"/><path d="M.5 2l4.5 3.5L9.5 2" stroke="#a51e2e" fill="none"/></svg>info@seelenweg-praxis.ch</li>
    <li><svg class="ic" viewBox="0 0 10 10"><circle cx="5" cy="5" r="4" stroke="#fff" fill="none"/><path d="M1 5h8M5 1c-2 2.5-2 5.5 0 8M5 1c2 2.5 2 5.5 0 8" stroke="#fff" fill="none" stroke-width=".7"/></svg>www.seelenweg-praxis.ch</li>
  </ul>
  <div class="badge badge--photo"><span class="badge__mark"></span>Lumen Harbor Circle</div>
  <div class="motto">Gesundheit - Glück - Liebe - Frieden</div>
</section>

<!-- Row 3 -->
<section class="card card--front" style="top:430px">
  <div class="arc"></div>
  <div class="brand brand--front"><span class="brand__dot"></span>Seelenweg</div>
  <div class="brand-sub brand-sub--front">Systemanalytiker</div>
  <div class="front-name">Udo Falkner</div>
  <div class="motto">Gesundheit - Glück - Liebe - Frieden</div>
</section>
<section class="card card--back" style="top:430px">
  <div class="arc"></div>
  <div class="panel"></div>
  <ul class="svc-list">
    <li>Psycho-Kinesiologie</li><li class="cont">nach Dr. Kellermann</li>
    <li>Neurobiologie</li><li>Mentalfeldtherapie</li><li>Geistiges Familienstellen</li>
  </ul>
  <ul class="contacts contacts--dark">
    <li><svg class="ic" viewBox="0 0 10 10"><path d="M2 1l2 2-1 1.5c.8 1.5 1.5 2.2 3 3L7.5 6l2 2-1.3 1.5C4.5 9 1 5.5.5 1.8z" fill="#fff"/></svg>Schweiz</li>
    <li class="gap">0041 790 482 615</li>
    <li><svg class="ic" viewBox="0 0 10 10"><path d="M2 1l2 2-1 1.5c.8 1.5 1.5 2.2 3 3L7.5 6l2 2-1.3 1.5C4.5 9 1 5.5.5 1.8z" fill="#fff"/></svg>Deutschland</li>
    <li class="gap">0049 170 264 81 93</li>
    <li><svg class="ic" viewBox="0 0 10 10"><rect x=".5" y="2" width="9" height="6" fill="#fff"/><path d="M.5 2l4.5 3.5L9.5 2" stroke="#a51e2e" fill="none"/></svg>info@seelenweg-praxis.ch</li>
    <li><svg class="ic" viewBox="0 0 10 10"><circle cx="5" cy="5" r="4" stroke="#fff" fill="none"/><path d="M1 5h8M5 1c-2 2.5-2 5.5 0 8M5 1c2 2.5 2 5.5 0 8" stroke="#fff" fill="none" stroke-width=".7"/></svg>www.seelenweg-praxis.ch</li>
  </ul>
  <div class="brand brand--dark"><span class="brand__dot"></span>Seelenweg</div>
  <div class="brand-sub brand-sub--dark">Systemanalytiker</div>
  <div class="person person--dark"><div class="person__name">Udo Falkner</div><div class="person__role">Systemanalytiker</div></div>
  <div class="badge badge--dark"><span class="badge__mark"></span>Lumen Harbor Circle</div>
  <div class="motto">Gesundheit - Glück - Liebe - Frieden</div>
</section>

<!-- Row 4 -->
<section class="card card--front" style="top:633px">
  <div class="pattern" role="img" aria-label="Dekoratives Blume-des-Lebens-Muster in Violett"></div>
  <div class="lettering" role="img" aria-label="Handschriftzug in Violett"></div>
  <div class="brand brand--front"><span class="brand__dot"></span>Seelenweg</div>
  <div class="brand-sub brand-sub--front">Systemanalytiker</div>
  <p class="services">Psycho-Kinesiologie nach Dr. Kellermann | Neurobiologie<br>Mentalfeldtherapie | Geistiges Familienstellen</p>
  <div class="motto">Gesundheit - Glück - Liebe - Frieden</div>
</section>
<section class="card card--back" style="top:633px">
  <div class="panel"></div>
  <div class="photo" role="img" aria-label="Schwarzweiß-Porträtfoto des Systemanalytikers"></div>
  <div class="brand brand--panel"><span class="brand__dot"></span>Seelenweg</div>
  <div class="brand-sub brand-sub--panel">Systemanalytiker</div>
  <div class="person"><div class="person__name">Udo Falkner</div><div class="person__role">Systemanalytiker</div></div>
  <ul class="contacts contacts--photo">
    <li><svg class="ic" viewBox="0 0 10 10"><path d="M2 1l2 2-1 1.5c.8 1.5 1.5 2.2 3 3L7.5 6l2 2-1.3 1.5C4.5 9 1 5.5.5 1.8z" fill="#fff"/></svg>Schweiz</li>
    <li class="gap">0041 790 482 615</li>
    <li><svg class="ic" viewBox="0 0 10 10"><path d="M2 1l2 2-1 1.5c.8 1.5 1.5 2.2 3 3L7.5 6l2 2-1.3 1.5C4.5 9 1 5.5.5 1.8z" fill="#fff"/></svg>Deutschland</li>
    <li class="gap">0049 170 264 81 93</li>
    <li><svg class="ic" viewBox="0 0 10 10"><rect x=".5" y="2" width="9" height="6" fill="#fff"/><path d="M.5 2l4.5 3.5L9.5 2" stroke="#a51e2e" fill="none"/></svg>info@seelenweg-praxis.ch</li>
    <li><svg class="ic" viewBox="0 0 10 10"><circle cx="5" cy="5" r="4" stroke="#fff" fill="none"/><path d="M1 5h8M5 1c-2 2.5-2 5.5 0 8M5 1c2 2.5 2 5.5 0 8" stroke="#fff" fill="none" stroke-width=".7"/></svg>www.seelenweg-praxis.ch</li>
  </ul>
  <div class="badge badge--photo"><span class="badge__mark"></span>Lumen Harbor Circle</div>
  <div class="motto">Gesundheit - Glück - Liebe - Frieden</div>
</section>

<!-- Row 5 -->
<section class="card card--front" style="top:820px">
  <div class="arc"></div>
  <div class="brand brand--front"><span class="brand__dot"></span>Seelenweg</div>
  <div class="brand-sub brand-sub--front">Systemanalytiker</div>
  <p class="services">Psycho-Kinesiologie nach Dr. Kellermann | Neurobiologie<br>Mentalfeldtherapie | Geistiges Familienstellen</p>
  <div class="motto">Gesundheit - Glück - Liebe - Frieden</div>
</section>
<section class="card card--back" style="top:820px">
  <div class="panel"></div>
  <div class="photo" role="img" aria-label="Schwarzweiß-Porträtfoto des Systemanalytikers"></div>
  <div class="brand brand--panel"><span class="brand__dot"></span>Seelenweg</div>
  <div class="brand-sub brand-sub--panel">Systemanalytiker</div>
  <div class="person"><div class="person__name">Udo Falkner</div><div class="person__role">Systemanalytiker</div></div>
  <ul class="contacts contacts--photo">
    <li><svg class="ic" viewBox="0 0 10 10"><path d="M2 1l2 2-1 1.5c.8 1.5 1.5 2.2 3 3L7.5 6l2 2-1.3 1.5C4.5 9 1 5.5.5 1.8z" fill="#fff"/></svg>Schweiz</li>
    <li class="gap">0041 790 482 615</li>
    <li><svg class="ic" viewBox="0 0 10 10"><path d="M2 1l2 2-1 1.5c.8 1.5 1.5 2.2 3 3L7.5 6l2 2-1.3 1.5C4.5 9 1 5.5.5 1.8z" fill="#fff"/></svg>Deutschland</li>
    <li class="gap">0049 170 264 81 93</li>
    <li><svg class="ic" viewBox="0 0 10 10"><rect x=".5" y="2" width="9" height="6" fill="#fff"/><path d="M.5 2l4.5 3.5L9.5 2" stroke="#a51e2e" fill="none"/></svg>info@seelenweg-praxis.ch</li>
    <li><svg class="ic" viewBox="0 0 10 10"><circle cx="5" cy="5" r="4" stroke="#fff" fill="none"/><path d="M1 5h8M5 1c-2 2.5-2 5.5 0 8M5 1c2 2.5 2 5.5 0 8" stroke="#fff" fill="none" stroke-width=".7"/></svg>www.seelenweg-praxis.ch</li>
  </ul>
  <div class="badge badge--photo"><span class="badge__mark"></span>Lumen Harbor Circle</div>
  <div class="motto">Gesundheit - Glück - Liebe - Frieden</div>
</section>

<!-- Row 6 -->
<section class="card card--front" style="top:1013px">
  <div class="arc"></div>
  <div class="brand brand--front"><span class="brand__dot"></span>Seelenweg</div>
  <div class="brand-sub brand-sub--front">Systemanalytiker</div>
  <div class="front-name">Udo Falkner</div>
  <div class="motto">Gesundheit - Glück - Liebe - Frieden</div>
</section>
<section class="card card--back" style="top:1013px">
  <div class="arc"></div>
  <div class="panel"></div>
  <ul class="svc-list">
    <li>Psycho-Kinesiologie</li><li class="cont">nach Dr. Kellermann</li>
    <li>Neurobiologie</li><li>Mentalfeldtherapie</li><li>Geistiges Familienstellen</li>
  </ul>
  <ul class="contacts contacts--dark">
    <li><svg class="ic" viewBox="0 0 10 10"><path d="M2 1l2 2-1 1.5c.8 1.5 1.5 2.2 3 3L7.5 6l2 2-1.3 1.5C4.5 9 1 5.5.5 1.8z" fill="#fff"/></svg>Schweiz</li>
    <li class="gap">0041 790 482 615</li>
    <li><svg class="ic" viewBox="0 0 10 10"><path d="M2 1l2 2-1 1.5c.8 1.5 1.5 2.2 3 3L7.5 6l2 2-1.3 1.5C4.5 9 1 5.5.5 1.8z" fill="#fff"/></svg>Deutschland</li>
    <li class="gap">0049 170 264 81 93</li>
    <li><svg class="ic" viewBox="0 0 10 10"><rect x=".5" y="2" width="9" height="6" fill="#fff"/><path d="M.5 2l4.5 3.5L9.5 2" stroke="#a51e2e" fill="none"/></svg>info@seelenweg-praxis.ch</li>
    <li><svg class="ic" viewBox="0 0 10 10"><circle cx="5" cy="5" r="4" stroke="#fff" fill="none"/><path d="M1 5h8M5 1c-2 2.5-2 5.5 0 8M5 1c2 2.5 2 5.5 0 8" stroke="#fff" fill="none" stroke-width=".7"/></svg>www.seelenweg-praxis.ch</li>
  </ul>
  <div class="brand brand--dark"><span class="brand__dot"></span>Seelenweg</div>
  <div class="brand-sub brand-sub--dark">Systemanalytiker</div>
  <div class="person person--dark"><div class="person__name">Udo Falkner</div><div class="person__role">Systemanalytiker</div></div>
  <div class="badge badge--dark"><span class="badge__mark"></span>Lumen Harbor Circle</div>
  <div class="motto">Gesundheit - Glück - Liebe - Frieden</div>
</section>

</body>
</html>
```